Kelmora - Step into Wonder! Business Card

We are bringing an amazing new system of dance to Australia and need a nifty, eye-catching little card that we can give to everyone to get them to come to class.

It needs a bit of information about Kelmora, along with contact details and a space for us to write a note for people about the next class.

Target Market(s)

30+ people that enjoy dance and are interested in self-development, meeting people and getting more out of life.

Industry/Entity Type

Business

Requirements
Must have
• Double sided in colour

A beautiful, simple design that indicates movement and is modern, fresh and uplifting.

The attached Kelmora logo

Text for the front :

Kelmora - the Step into Wonder

Dance from your heart and feel your life open.

Regular classes in Sydney and Canberra with Mara Polden and Torsten Walby

Text for the back :

Kelmora ignites our vital spark for life and awakens our innate potential for pleasurable, joyful, heartfelt living through dance, music and authentic connection.

Torsten and Mara are committed to offering authentic, supportive and inspiring spaces for your growth through Kelmora.

Contact us on mara@kelmora.com.au - twbyrne@mailquest.net or 0491 570 284.

www.kelmora.com.au

Nice to have
• Some movement in the design

Use some of the photos attached in some form - could be faded, incorporated into design etc.

Creative use of the logo - integrating it within the design - e.g perhaps using it as the O in Kelmora,
Should not have
• Not a lot of black

```html
<!DOCTYPE html>
<html lang="en">
<head>
<meta charset="utf-8">
<title>Kelmora Business Card</title>
<link href="https://fonts.googleapis.com/css2?family=Didact+Gothic&family=IM+Fell+English:ital@1&display=swap" rel="stylesheet">
<style>
  :root {
    --backdrop: #e9e6e1;
    --card: #ffffff;
    --ink: #5a5652;
    --ink-soft: #6d6862;
    --paper-glow: #fdfbf6;
    --photo-maroon: #6b2a3a;
    --photo-cream: #e8dcc0;
    --photo-brown: #3a2620;
    --photo-wine: #9a4a5c;
    --photo-stone: #7d6a5c;
    --photo-shadow: #2c2420;
    --photo-mint: #cfe0cf;
    --photo-amber: #c9a878;
  }
  * { box-sizing: border-box; margin: 0; padding: 0; }
  html, body { width: 1200px; height: 900px; overflow: hidden; }
  body {
    background: var(--backdrop);
    font-family: "Didact Gothic", "Century Gothic", sans-serif;
    color: var(--ink);
    position: relative;
  }

  .card {
    position: absolute;
    width: 600px;
    height: 366px;
    background: var(--card);
    box-shadow: 0 10px 28px rgba(0,0,0,.18);
    overflow: hidden;
  }
  .card--front { left: 120px; top: 60px; }
  .card--back  { left: 480px; top: 474px; }

  /* FRONT */
  .front-photo {
    position: absolute;
    left: 16px; top: 14px; right: 16px; bottom: 24px;
    border-top-left-radius: 26px;
    background:
      radial-gradient(ellipse 30% 45% at 18% 75%, var(--photo-wine) 0%, transparent 70%),
      radial-gradient(ellipse 35% 40% at 60% 30%, var(--photo-cream) 0%, transparent 75%),
      radial-gradient(ellipse 25% 35% at 85% 55%, var(--photo-cream) 0%, transparent 75%),
      linear-gradient(120deg, var(--photo-maroon) 0%, var(--photo-brown) 45%, var(--photo-maroon) 70%, var(--photo-brown) 100%);
  }
  .front-logo {
    position: absolute;
    left: 44px; top: 58px;
    width: 150px; height: 150px;
    border-radius: 50%;
    background: var(--card);
    display: flex; align-items: center; justify-content: center;
    box-shadow: 0 0 0 3px rgba(255,255,255,.5);
  }
  .front-logo__name {
    font-size: 24px;
    color: var(--ink);
    letter-spacing: 1px;
  }
  .front-label {
    position: absolute;
    left: 222px; top: 72px;
    padding: 6px 14px;
    background: var(--card);
    font-size: 13px;
    color: var(--ink);
  }
  .front-tagline {
    position: absolute;
    left: 228px; top: 108px;
    width: 300px;
    font-family: "IM Fell English", Georgia, serif;
    font-style: italic;
    font-size: 25px;
    line-height: 1.2;
    color: var(--paper-glow);
    text-align: center;
    text-shadow: 0 1px 3px rgba(0,0,0,.6);
  }
  .front-band {
    position: absolute;
    left: 16px; right: 16px; top: 266px;
    height: 38px;
    background: var(--card);
    display: flex; align-items: center;
    padding-left: 18px;
    font-size: 15px;
    color: var(--ink-soft);
  }

  /* BACK */
  .back-photo {
    position: absolute;
    left: 16px; top: 16px; right: 16px; bottom: 18px;
    border-bottom-left-radius: 26px;
    background:
      radial-gradient(ellipse 22% 40% at 48% 55%, var(--photo-shadow) 0%, transparent 75%),
      radial-gradient(ellipse 30% 30% at 70% 85%, var(--photo-mint) 0%, transparent 75%),
      radial-gradient(ellipse 20% 30% at 95% 75%, var(--photo-amber) 0%, transparent 80%),
      linear-gradient(180deg, var(--photo-stone) 0%, #5e4a40 40%, #4a3a34 70%, #8c7a6c 100%);
  }
  .back-about {
    position: absolute;
    left: 36px; top: 96px;
    width: 250px; height: 170px;
    background: var(--card);
    clip-path: polygon(0 10%, 62% 0, 70% 9%, 100% 3%, 94% 38%, 100% 58%, 95% 100%, 40% 93%, 0 100%, 4% 55%);
    padding: 30px 28px 20px 20px;
    font-size: 14px;
    line-height: 1.3;
    color: var(--ink-soft);
  }
  .back-contact {
    position: absolute;
    right: 30px; top: 52px;
    width: 250px; height: 120px;
    background: var(--card);
    clip-path: polygon(0 30%, 12% 22%, 8% 0, 100% 0, 100% 100%, 14% 92%, 4% 70%, 10% 55%);
    padding: 36px 18px 0 0;
    text-align: right;
    font-size: 12.5px;
    line-height: 1.35;
    color: var(--ink-soft);
  }
  .back-contact__icon {
    position: absolute;
    left: 48px; top: 14px;
    width: 26px; height: 26px;
  }
  .back-band {
    position: absolute;
    left: 16px; right: 16px; top: 270px;
    height: 52px;
    background: var(--card);
    display: flex; align-items: center; justify-content: center;
    text-align: center;
    padding: 0 30px;
    font-size: 14px;
    line-height: 1.35;
    color: var(--ink-soft);
  }
</style>
</head>
<body>

<section class="card card--front" aria-label="Kelmora card front">
  <div class="front-photo" role="img" aria-label="Warm, faded photograph of people dancing together in a class"></div>
  <div class="front-logo"><span class="front-logo__name">Kelmora</span></div>
  <div class="front-label">Kelmora - the Step into Wonder</div>
  <p class="front-tagline">Dance from your heart and<br>feel your life open.</p>
  <div class="front-band">Regular classes in Sydney and Canberra with Mara Polden and Torsten Walby</div>
</section>

<section class="card card--back" aria-label="Kelmora card back">
  <div class="back-photo" role="img" aria-label="Soft, faded photograph of a dancer moving in a studio"></div>
  <div class="back-about">Kelmora ignites our vital spark for life and awakens our innate potential for pleasurable, joyful, heartfelt living through dance, music and authentic connection.</div>
  <div class="back-contact">
    <svg class="back-contact__icon" viewBox="0 0 26 26" aria-hidden="true">
      <path d="M3 9 Q3 4 13 4 Q23 4 23 9 L23 11 L18 11 L18 8.5 L8 8.5 L8 11 L3 11 Z" fill="#222"/>
      <path d="M7 12 L19 12 L22 22 L4 22 Z" fill="#222"/>
      <rect x="9" y="14" width="8" height="5" fill="#fff"/>
    </svg>
    mara@kelmora.com.au<br>
    twbyrne@mailquest.net<br>
    0491 570 284
  </div>
  <div class="back-band">Torsten and Mara are committed to offering authentic, supportive and inspiring spaces for your growth through Kelmora.</div>
</section>

</body>
</html>
```